Family Farm Looking for meat label

We have a small farm in Italy with two types of cow "Piemontese" and "Pezzata Rossa Valdostana". We need label ( about 5x5 cm) to put on the boxes and on every single piece of meat.

Target Market(s)

private client

Industry/Entity Type

family farm

Colors

Designer to choose colors to be used in the design.

Requirements
Must have
• to write "Azienda Agricola Il Roveto" and the cow like our cow not differently. the Piemontese breed cow has the typical physical shapes as in the photo. No photo on the label just a drawing o something like that.
Nice to have
• just a one label, clear, fine and clean . Maybe with pastel color or watercolor. We are a small family farm.
Should not have
• no photo, no another type of cow

```html
<!DOCTYPE html>
<html lang="it">
<head>
<meta charset="utf-8">
<title>Azienda Agricola Il Roveto – Etichetta</title>
<link rel="stylesheet" href="https://fonts.googleapis.com/css2?family=Roboto+Condensed:wght@700&family=Uncial+Antiqua&display=swap">
<style>
  :root {
    --backdrop: #cbdeeb;
    --sky: #0096dc;
    --sky-deep: #0a84c2;
    --meadow: #6db644;
    --poppy: #ec2a22;
    --cloud: #eef3f7;
    --bull-coat: #dcdcd8;
    --bull-shade: #a9aba7;
    --cow-coat: #5a2e26;
    --ink-light: #ffffff;
  }
  html, body {
    margin: 0;
    padding: 0;
    width: 1200px;
    height: 1200px;
    overflow: hidden;
    background: var(--backdrop);
  }
  .label {
    position: absolute;
    left: 266px;
    top: 270px;
    width: 664px;
    height: 664px;
    filter: drop-shadow(8px 8px 6px rgba(60, 70, 80, 0.45));
  }
  .label svg { display: block; width: 100%; height: 100%; }
  .brand-name {
    font-family: "Roboto Condensed", "Arial Narrow", sans-serif;
    font-weight: 700;
    font-size: 64px;
    fill: var(--ink-light);
  }
  .headline {
    font-family: "Uncial Antiqua", serif;
    fill: var(--ink-light);
  }
  .headline-top { font-size: 84px; }
  .headline-bottom { font-size: 82px; }
  .flourish { stroke: var(--ink-light); stroke-width: 6; stroke-linecap: round; fill: none; }
</style>
</head>
<body>
  <div class="label">
    <svg viewBox="0 0 1069 1068" xmlns="http://www.w3.org/2000/svg">
      <defs>
        <linearGradient id="sky-fill" x1="0" y1="0" x2="0" y2="1">
          <stop offset="0" stop-color="var(--sky)"/>
          <stop offset="0.55" stop-color="var(--sky-deep)"/>
          <stop offset="1" stop-color="#3a97d2"/>
        </linearGradient>
        <linearGradient id="herd-fill" x1="0" y1="0" x2="1" y2="0">
          <stop offset="0" stop-color="var(--cloud)"/>
          <stop offset="0.1" stop-color="var(--bull-coat)"/>
          <stop offset="0.38" stop-color="var(--bull-shade)"/>
          <stop offset="0.55" stop-color="#8a6a5e"/>
          <stop offset="0.72" stop-color="var(--cow-coat)"/>
          <stop offset="0.9" stop-color="#c9d3dc"/>
          <stop offset="1" stop-color="var(--cloud)"/>
        </linearGradient>
      </defs>

      <rect class="sky" x="0" y="0" width="1069" height="1068" fill="url(#sky-fill)"/>

      <path class="roof-band" d="M0 0 H502 L183 192 H0 Z" fill="var(--meadow)"/>
      <path class="roof-band" d="M529 0 H1069 V192 H844 Z" fill="var(--meadow)"/>

      <circle class="brand-dot" cx="510" cy="100" r="11" fill="none" stroke="var(--ink-light)" stroke-width="3"/>
      <text class="brand-name" x="510" y="225" text-anchor="middle">IL ROVETO</text>

      <path id="arc-top" d="M95 500 Q530 300 965 500" fill="none"/>
      <path id="arc-bottom" d="M285 530 Q530 450 790 535" fill="none"/>
      <text class="headline headline-top"><textPath href="#arc-top" startOffset="50%" text-anchor="middle">AZIENDA AGRICOLA</textPath></text>
      <text class="headline headline-bottom"><textPath href="#arc-bottom" startOffset="50%" text-anchor="middle">IL ROVETO</textPath></text>
      <line class="flourish" x1="142" y1="552" x2="240" y2="519"/>
      <line class="flourish" x1="815" y1="516" x2="925" y2="552"/>

      <rect class="herd-scene" x="0" y="648" width="1069" height="352" fill="url(#herd-fill)" opacity="0.9" role="img" aria-label="Illustrazione: un toro di razza Piemontese bianco e una vacca Pezzata Rossa Valdostana su un prato, sotto un cielo con nuvole"/>

      <path class="hill-red" d="M0 968 Q330 958 660 992 L0 1068 Z" fill="var(--poppy)"/>
      <path class="hill-green" d="M660 992 L1069 964 V1068 H0 Z" fill="var(--meadow)"/>
    </svg>
  </div>
</body>
</html>
```